Voranel.com Personal Trainer/Fitness Website

I want a website to market my personal training/Outdoor Bootcamp Class services, as well as to ditribute nutrivexa. I need a logo as well I included an address for the Harbor Gales 1975 logo. I'd like Voranel in place of Harbor Gales, and in Black and white, just different enough so I can't get sued by the PLX.
https://www.pictofind.example/imgres?imgurl=http%3A%2F%2Fwww.dorian-halverstock.example%2Fwp-content%2Fuploads%2F2014%2F01%2Fgales_mark4.jpg&imgrefurl=http%3A%2F%2Fwww.dorian-halverstock.example%2Fplx-emblem-reworks-tulsa-harbor-bolts%2F&docid=_qweRT8uPLmnBx&tbnid=k3tyA7XbNqwePZ%3A&w=600&h=450&client=ms-android-carrierx&bih=512&biw=360&ved=0ahUKEwiQazxcv7LMAhUTwGMKHRPMBWMQMwg6KBQwFA&iact=mrc&uact=8.
It should be about 5 pages 1. home 2. about 3. Services 4. Blog/Videos and programs 5. Contact.
http://www.tobenwelfitness.example.uk/ is a website I like the style of.

Target Market(s)

Seattle area

Industry/Entity Type

Fitness

Coding

Coded - Design and coding required

Number of Pages Required

4 page

Font styles to use
Serif
Sans Serif

Requirements
Must have
• A minimal look
Nice to have
• A logo similar to the 1975 Harbor Galewinds Logo, with a Small Dorn Velask ripping his shirt open(with a picture of the logo on his shirt, picture within picture) to turn into Skyvaler in the center. Skyline is black, Background and small figure white(with black logo on shirt)

```html
<!DOCTYPE html>
<html lang="en">
<head>
<meta charset="utf-8">
<title>Voranel – Personal Trainer Mayfair</title>
<link href="https://fonts.googleapis.com/css2?family=Ubuntu:wght@400;500;700&family=Varela+Round&family=Tinos&display=swap" rel="stylesheet">
<style>
  :root {
    --ink: #231f20;
    --paper: #ffffff;
    --stage: #f2f2f2;
    --band: #e6e6e6;
    --muted: #c9c9c9;
    --body-text: #1f1f1f;
    --hero-a: #4a3a32;
    --hero-b: #8a5a3c;
    --hero-c: #2f3440;
    --photo-a: #c9d6dc;
    --photo-b: #6f5a4c;
  }
  * { box-sizing: border-box; margin: 0; padding: 0; }
  html, body { width: 1200px; height: 1000px; overflow: hidden; }
  body {
    background: var(--stage);
    font-family: "Varela Round", "Helvetica Neue", Arial, sans-serif;
    color: var(--body-text);
    position: relative;
  }
  .page {
    position: absolute;
    left: 220px; top: 23px;
    width: 634px; height: 795px;
    background: var(--paper);
    transform: scale(1.2);
    transform-origin: top left;
    box-shadow: 0 6px 18px rgba(0,0,0,.25);
    overflow: hidden;
  }
  /* top utility bar */
  .utility-bar {
    position: absolute; left: 0; top: 0; width: 100%; height: 28px;
    background: var(--ink); color: var(--paper);
    font-family: "Ubuntu", sans-serif; font-size: 7px; font-weight: 700;
  }
  .utility-bar .call { position: absolute; left: 25px; top: 10px; }
  .utility-bar .social { position: absolute; left: 470px; top: 9px; display: flex; gap: 8px; align-items: center; }
  .social-dot { width: 9px; height: 9px; border: 1.2px solid var(--paper); border-radius: 50%; }
  .utility-bar .search { position: absolute; left: 565px; top: 10px; font-weight: 500; }
  .utility-bar .search-icon { position: absolute; left: 600px; top: 7px; }
  /* header */
  .site-header { position: absolute; left: 0; top: 28px; width: 100%; height: 86px; }
  .brand {
    position: absolute; left: 45px; top: 31px;
    display: flex; align-items: center; gap: 6px;
    font-family: "Ubuntu", sans-serif; font-weight: 700; font-size: 15px;
    letter-spacing: 1.5px; color: var(--ink);
  }
  .brand-dot { width: 12px; height: 12px; border-radius: 50%; background: var(--ink); }
  .main-nav {
    position: absolute; right: 53px; top: 44px;
    display: flex; gap: 7px;
    font-family: "Ubuntu", sans-serif; font-weight: 700; font-size: 7.6px; color: var(--ink);
  }
  /* hero */
  .hero { position: absolute; left: 0; top: 114px; width: 100%; height: 210px; }
  .hero-photo {
    position: absolute; inset: 0;
    background:
      radial-gradient(ellipse at 38% 55%, var(--hero-b) 0%, transparent 45%),
      radial-gradient(ellipse at 65% 45%, #9a6848 0%, transparent 40%),
      linear-gradient(90deg, var(--hero-a), #6b5446 40%, #5b4a40 60%, var(--hero-c));
    filter: saturate(.9);
  }
  .hero-shade { position: absolute; inset: 0; background: rgba(0,0,0,.18); }
  .hero-copy { position: absolute; left: 0; width: 100%; text-align: center; color: var(--paper); }
  .hero-sub { top: 72px; font-family: "Ubuntu", sans-serif; font-weight: 500; font-size: 9px; }
  .hero-title { top: 96px; font-family: "Ubuntu", sans-serif; font-weight: 500; font-size: 17.5px; letter-spacing: .3px; }
  .hero-button {
    position: absolute; left: 256px; top: 134px; width: 121px; height: 30px;
    border: 2px solid var(--paper); color: var(--paper);
    font-family: "Ubuntu", sans-serif; font-weight: 500; font-size: 13px;
    display: flex; align-items: center; justify-content: center;
  }
  /* about */
  .about { position: absolute; left: 0; top: 324px; width: 100%; height: 240px; }
  .trainer-photo {
    position: absolute; left: 33px; top: 49px; width: 152px; height: 154px; border-radius: 50%;
    background: radial-gradient(circle at 50% 40%, var(--photo-b) 0 22%, var(--photo-a) 23% 60%, #2a2a2a 61%);
  }
  .about-text { position: absolute; left: 207px; top: 38px; width: 392px; }
  .about-text h2 { font-family: "Ubuntu", sans-serif; font-weight: 400; font-size: 14.5px; color: var(--ink); margin-bottom: 4px; }
  .about-text p { font-size: 8.2px; line-height: 9.6px; margin-bottom: 9.6px; }
  /* services */
  .services {
    position: absolute; left: 0; top: 564px; width: 100%; height: 126px; background: var(--band);
  }
  .service { position: absolute; top: 18px; width: 180px; text-align: center; }
  .service .icon {
    width: 46px; height: 46px; border-radius: 50%; background: var(--ink);
    margin: 0 auto 7px; display: flex; align-items: center; justify-content: center;
  }
  .service h3 { font-family: "Ubuntu", sans-serif; font-weight: 400; font-size: 9.5px; margin-bottom: 3px; }
  .service p { font-family: "Tinos", "Times New Roman", serif; font-size: 7.6px; line-height: 9.5px; }
  /* footer */
  .site-footer {
    position: absolute; left: 0; top: 720px; width: 100%; height: 75px;
    background: var(--ink); color: var(--paper);
  }
  .footer-col { position: absolute; top: 11px; font-size: 7.4px; line-height: 12px; }
  .footer-col h4 { font-family: "Ubuntu", sans-serif; font-weight: 700; font-size: 8.6px; margin-bottom: 1px; }
  .footer-col li { list-style: none; }
  .footer-col.contact li, .footer-col.location li { line-height: 10px; }
</style>
</head>
<body>
<div class="page">

  <div class="utility-bar">
    <span class="call">Call Today: 0000 000 000</span>
    <div class="social">
      <span class="social-dot"></span>
      <span class="social-dot"></span>
      <svg width="11" height="9" viewBox="0 0 11 9" aria-label="Email">
        <rect x=".6" y=".6" width="9.8" height="7.8" fill="none" stroke="#fff" stroke-width="1.1"/>
        <path d="M.6 .8 L5.5 5 L10.4 .8" fill="none" stroke="#fff" stroke-width="1.1"/>
      </svg>
    </div>
    <span class="search">Search</span>
    <svg class="search-icon" width="14" height="14" viewBox="0 0 14 14" aria-label="Search">
      <circle cx="8.5" cy="5.5" r="4.3" fill="none" stroke="#fff" stroke-width="1.4"/>
      <path d="M5.4 8.6 L1 13" stroke="#fff" stroke-width="1.6"/>
    </svg>
  </div>

  <header class="site-header">
    <div class="brand"><span class="brand-dot"></span>VORANEL</div>
    <nav class="main-nav">
      <span>HOME</span><span>ABOUT</span><span>SERVICES</span><span>BLOG</span><span>CONTACT</span>
    </nav>
  </header>

  <section class="hero">
    <div class="hero-photo" role="img" aria-label="Blurred photo of a trainer coaching a client lifting dumbbells in a gym"></div>
    <div class="hero-shade"></div>
    <p class="hero-copy hero-sub">Premium personal training services in the Mayfair area</p>
    <h1 class="hero-copy hero-title">PERSONAL TRAINER MAYFAIR</h1>
    <div class="hero-button">GET IN TOUCH</div>
  </section>

  <section class="about">
    <div class="trainer-photo" role="img" aria-label="Round portrait photo of the personal trainer in a gym"></div>
    <div class="about-text">
      <h2>Personal Training in Voranel</h2>
      <p>I work exclusively with men and women who are trying to make a difference in their personal lives. Working long hours can make it hard to find time to build your stamina, shred muscle and lose some weight.</p>
      <p>My personal training studio in Mayfair is conveniently located under Hotel Calverin. This is not another noisy gym that will let you down by forcing you to try and figure it out on your own. Let me guide you with my knowledge, and keep you engaged with fun workouts that will get you in the best shape of your life.</p>
      <p>You have everything to gain from incorporating a holistic approach to health and fitness. My personality and style of training are infectious, and my forward vision is to “infect” you into a healthy way of thinking and way of life. Holiday season is never too far away. How do you want to look on the beach this year?</p>
    </div>
  </section>

  <section class="services">
    <div class="service" style="left:47px">
      <div class="icon">
        <svg width="30" height="16" viewBox="0 0 30 16" aria-label="Dumbbell">
          <g fill="#fff">
            <rect x="1" y="5" width="2" height="6"/><rect x="4" y="1" width="3" height="14"/>
            <rect x="8" y="3" width="2" height="10"/><rect x="10" y="7" width="10" height="2"/>
            <rect x="20" y="3" width="2" height="10"/><rect x="23" y="1" width="3" height="14"/>
            <rect x="27" y="5" width="2" height="6"/>
          </g>
        </svg>
      </div>
      <h3>Personal Training</h3>
      <p>Private Personal Training<br>100% Customized Exercise Programming<br>Customized Nutrition and Supplementation</p>
    </div>
    <div class="service" style="left:227px">
      <div class="icon">
        <svg width="26" height="18" viewBox="0 0 26 18" aria-label="Laptop">
          <rect x="4" y="1" width="18" height="12" rx="1" fill="none" stroke="#fff" stroke-width="2"/>
          <rect x="1" y="14" width="24" height="3" rx="1" fill="#fff"/>
        </svg>
      </div>
      <h3>Online Coaching</h3>
      <p>Personal Training From A Distance<br>24 Hour Support and Contact<br>Customized Nutrition and Supplementation</p>
    </div>
    <div class="service" style="left:407px">
      <div class="icon">
        <svg width="30" height="20" viewBox="0 0 30 20" aria-label="Group">
          <g fill="#fff">
            <circle cx="7" cy="6" r="3"/><path d="M1 18 Q1 10 7 10 Q13 10 13 18Z"/>
            <circle cx="23" cy="6" r="3"/><path d="M17 18 Q17 10 23 10 Q29 10 29 18Z"/>
            <circle cx="15" cy="5" r="3.6" stroke="#231f20" stroke-width="1"/>
            <path d="M8 20 Q8 10 15 10 Q22 10 22 20Z" stroke="#231f20" stroke-width="1"/>
          </g>
        </svg>
      </div>
      <h3>Small Group</h3>
      <p>Work with 2-3 of Your Friends<br>Boot Camp Style Personal Training<br>Customized Nutrition and Supplementation</p>
    </div>
  </section>

  <footer class="site-footer">
    <div class="footer-col" style="left:180px">
      <h4>Nagivation</h4>
      <ul><li>Home</li><li>Services</li><li>Blog</li><li>Contact</li></ul>
    </div>
    <div class="footer-col contact" style="left:296px">
      <h4>Contact</h4>
      <ul><li>Phone: 00000 000 000</li><li>Email: contact@voranel.example</li></ul>
    </div>
    <div class="footer-col location" style="left:412px">
      <h4>Location</h4>
      <ul><li>Hotel Calverin</li><li>48 Harrowgate Row</li><li>London</li><li>W2K 7QP</li></ul>
    </div>
  </footer>

</div>
</body>
</html>
```